Website design for legal tech start up in Switzerland (B2B)

We are for a legal tech start up in Switzerland called DRAVIQ. We have been running since August 2016. This will be our first live website.

We need a website designed and business card design for our start-up in Switzerland. We also need the Web design to be converted into HTML and CSS files.

Function of website:
• To inform potential customers of our services
• Form a key part of our digital marketing and sales footprint.
• Branding

Please find attached logo.

Reason: Looking for more idea's not necessarily set on blue and grey colours only.

Target Market(s)

B2B tech powered legal services.

Industry/Entity Type

Legal

Contact Information for Business Card

Lean and slick design.

Coding

Coded - Design and coding required

Number of Pages Required

5+ page

Requirements
Must have
• VERY LEAN AND CLEAN DESIGN!
• We have received many great standard designs, but we are looking for something more out-of-the box: You can get inspiration from these designs: http://www.plimbergallery.net/websites/clean/
• Thanks!!
• Easy content management system
• Well structured coding for additional development
• Responsive webpage for all types of devices
• SEO optimized
• Tabs (Home, services, team, careers, blog, contact us)
• Colour scheme complementary to logo
Nice to have
• Look and Design - Approachable, High-tech, Modern
• Easy to add chat bot capability in future
Should not have
• Too busy/ too much clutter
• Not take to long to load

```html
<!DOCTYPE html>
<html lang="en">
<head>
<meta charset="utf-8">
<title>DRAVIQ — Legal Services</title>
<link href="https://fonts.googleapis.com/css2?family=Lato:wght@300;400;700;900&display=swap" rel="stylesheet">
<style>
:root{
  --navy:#1f3b6e;
  --ink:#2f3437;
  --text:#6b6f73;
  --charcoal:#454545;
  --panel:#e8e9eb;
  --footer:#d9dadc;
  --line:#d6d7d9;
  --white:#ffffff;
}
*{margin:0;padding:0;box-sizing:border-box}
html,body{width:1200px;height:3035px;overflow:hidden}
body{position:relative;background:var(--white);font-family:'Lato',sans-serif;color:var(--ink)}
.abs{position:absolute}
.photo{position:absolute}

/* header */
.brand{left:87px;top:40px;font-size:44px;font-weight:900;letter-spacing:3px;color:var(--charcoal);line-height:1;white-space:nowrap}
.nav{left:526px;top:36px;width:587px;height:53px;background:var(--charcoal);clip-path:polygon(40px 0,100% 0,100% 100%,0 100%);display:flex;justify-content:flex-end;align-items:center;gap:34px;padding-right:26px}
.nav a{color:var(--white);text-decoration:none;font-size:17px}

/* hero */
.hero{left:0;top:105px;width:1200px;height:453px;background:linear-gradient(100deg,#3a3633 0%,#5b5047 35%,#4a4038 60%,#2e2a27 100%)}
.hero-shade{left:0;top:105px;width:1200px;height:453px;background:rgba(20,20,25,.35)}
.hero-title{left:0;width:1200px;top:236px;text-align:center;color:var(--white);font-size:56px;font-weight:900;letter-spacing:1px;white-space:nowrap}
.hero-sub{left:0;width:1200px;top:302px;text-align:center;color:var(--white);font-size:17px;line-height:24px}
.btn-outline{left:520px;top:368px;width:162px;height:51px;border:2px solid var(--white);color:var(--white);font-size:17px;display:flex;align-items:center;justify-content:center}
.dots{left:562px;top:476px;display:flex;gap:8px}
.dots span{width:17px;height:17px;border:2px solid var(--white);border-radius:50%}
.dots span.on{background:var(--white)}

/* about */
.about-photo{left:87px;top:601px;width:389px;height:437px;background:linear-gradient(160deg,#e9eef2 0%,#d7c2a8 45%,#3a2e2a 100%)}
.about-box{left:461px;top:670px;width:652px;height:297px;background:var(--panel)}
.h-section{font-size:27px;font-weight:400;color:var(--ink);letter-spacing:.5px;white-space:nowrap}
.h-rule{width:74px;height:2px;background:var(--navy);margin-top:6px}
.about-head{left:506px;top:698px}
.about-text{left:506px;top:752px;width:570px;font-size:12.5px;line-height:22px;color:var(--text)}
.btn-navy{background:var(--navy);color:var(--white);display:flex;align-items:center;justify-content:center}
.about-btn{left:506px;top:886px;width:158px;height:47px;font-size:17px}

/* services */
.services-photo{left:627px;top:1018px;width:486px;height:506px;background:linear-gradient(120deg,#e4ddd4 0%,#c7d6e6 40%,#a7744f 75%,#6b4a33 100%);clip-path:polygon(90px 0,100% 0,100% 100%,0 100%,0 170px)}
.services-box{left:85px;top:1089px;width:652px;height:372px;background:var(--white);border:1px solid #cfd0d2}
.services-head{left:129px;top:1117px}
.service{top:1196px;width:210px;text-align:center}
.service .ring{width:102px;height:102px;margin:0 auto;border-radius:50%;border:2px solid #555;display:flex;align-items:center;justify-content:center}
.service.featured .ring{background:var(--navy);border-color:var(--navy);box-shadow:inset 0 0 0 4px var(--white)}
.service h3{margin-top:18px;font-size:15px;font-weight:400;color:var(--ink);letter-spacing:.3px}
.service.featured h3{color:var(--navy)}
.service p{margin-top:4px;font-size:12.5px;line-height:18px;color:#555}

/* ribbons */
.ribbon{left:85px;width:381px;height:79px;background:var(--navy);clip-path:polygon(0 0,100% 0,82% 100%,0 100%);color:var(--white);font-size:27px;display:flex;align-items:center;padding-left:72px}

/* team */
.member{top:1645px;height:397px}
.member .portrait{position:absolute;left:0;top:0;right:0;height:308px}
.member .plate{position:absolute;left:0;right:0;bottom:0;height:89px;background:var(--charcoal);color:var(--white);text-align:center;padding-top:22px}
.plate h4{font-size:17px;font-weight:700;letter-spacing:.5px}
.plate span{display:block;margin-top:6px;font-size:12px;letter-spacing:.5px}
.member.active .portrait::after{content:"";position:absolute;inset:0;background:rgba(70,70,70,.6)}
.view-icon{position:absolute;left:50%;top:120px;transform:translateX(-50%);z-index:2}

/* news */
.news{top:2198px;width:326px;height:445px;border:2px solid var(--line);background:var(--white)}
.news.active{border-color:#bdbec0}
.news .thumb{position:absolute;left:6px;top:6px;right:6px;height:239px}
.news .date{position:absolute;right:14px;top:18px;background:#2d2d2d;color:var(--white);font-size:12.5px;padding:7px 12px;z-index:2}
.news.active .date{background:var(--navy)}
.news h5{position:absolute;left:18px;top:272px;font-size:17px;font-weight:700;color:var(--ink);white-space:nowrap}
.news p{position:absolute;left:18px;top:304px;width:290px;font-size:12.5px;line-height:19px;color:#555}
.news .more{position:absolute;left:18px;top:374px;width:92px;height:33px;background:var(--charcoal);color:var(--white);font-size:12.5px;display:flex;align-items:center;justify-content:center}
.news.active .more{background:var(--navy)}

/* footer */
.footer{left:0;top:2732px;width:1200px;height:243px;background:var(--footer)}
.footer-brand{left:87px;top:2780px;font-size:44px;font-weight:900;letter-spacing:3px;color:var(--charcoal);line-height:1;white-space:nowrap}
.subscribe{left:85px;top:2861px;width:251px;height:45px;display:flex}
.subscribe .field{flex:1;background:var(--white);font-size:12px;color:#777;display:flex;align-items:center;padding-left:14px}
.subscribe .send{width:43px;background:var(--navy);display:flex;align-items:center;justify-content:center}
.foot-head{font-size:21px;font-weight:400;color:var(--ink)}
.reach{left:514px;top:2776px}
.reach ul{list-style:none;margin-top:18px}
.reach li{font-size:12.5px;color:var(--ink);display:flex;align-items:center;gap:8px;height:32px}
.links{left:967px;top:2776px}
.links .cols{display:flex;gap:34px;margin-top:18px}
.links ul{list-style:none}
.links li{font-size:12.5px;line-height:22px;color:var(--ink)}
.bottom{left:0;top:2975px;width:1200px;height:60px;background:var(--navy)}
.copy{left:87px;top:2998px;color:var(--white);font-size:12.5px}
.social{left:555px;top:2997px;display:flex;gap:16px}
.social span{width:16px;height:16px;border-radius:50%;background:var(--white)}
</style>
</head>
<body>

<div class="abs brand">DRAVIQ</div>
<nav class="abs nav">
  <a>Home</a><a>Services</a><a>Team</a><a>Careers</a><a>Blog</a><a>Contact Us</a>
</nav>

<div class="photo hero" role="img" aria-label="Business team meeting around a table in an office"></div>
<div class="abs hero-shade"></div>
<h1 class="abs hero-title">WELCOME TO DRAVIQ</h1>
<p class="abs hero-sub">But I must explain to you how all this mistaken idea of denouncing pleasure and<br>praising pain was born and I will give you a complete account of the system</p>
<div class="abs btn-outline">READ MORE</div>
<div class="abs dots"><span></span><span class="on"></span><span></span></div>

<div class="photo about-photo" role="img" aria-label="Portrait of a smiling businesswoman in glasses"></div>
<div class="abs about-box"></div>
<div class="abs about-head"><h2 class="h-section">ABOUT DRAVIQ</h2><div class="h-rule"></div></div>
<p class="abs about-text">Lorem ipsum dolor sit amet, consectetur adipiscing elit, sed do eiusmod tempor incididunt ut labore et dolore magna aliqua. Ut enim ad minim veniam, quis nostrud exercitation ullamco laboris nisi ut aliquip ex ea commodo consequat. Duis aute irure dolor in reprehenderit in voluptate velit esse cillum dolore eu fugiat nulla pariatur. Excepteur sint occaecat cupidatat non proident, sunt in culpa qui officia deserunt mollit anim id est laborum.</p>
<div class="abs btn-navy about-btn">READ MORE</div>

<div class="photo services-photo" role="img" aria-label="Colleagues discussing work at a desk"></div>
<div class="abs services-box"></div>
<div class="abs services-head"><h2 class="h-section">OUR SERVICES</h2><div class="h-rule"></div></div>

<div class="abs service" style="left:101px">
  <div class="ring">
    <svg width="56" height="56" viewBox="0 0 56 56" fill="#555"><circle cx="24" cy="20" r="8"/><path d="M8 50c0-10 7-16 16-16s16 6 16 16z"/><rect x="34" y="6" width="18" height="12" rx="2"/></svg>
  </div>
  <h3>CONSULTING</h3>
  <p>Lorem ipsum dolor sit amet,<br>consectetur adipiscing elit, sed<br>do eiusmod tempor</p>
</div>
<div class="abs service featured" style="left:310px">
  <div class="ring">
    <svg width="52" height="52" viewBox="0 0 52 52" fill="#fff"><path d="M26 6 6 16h40z"/><rect x="9" y="20" width="5" height="20"/><rect x="19" y="20" width="5" height="20"/><rect x="28" y="20" width="5" height="20"/><rect x="38" y="20" width="5" height="20"/><rect x="6" y="42" width="40" height="5"/></svg>
  </div>
  <h3>SPECIAL SERVICES</h3>
  <p>Lorem ipsum dolor sit amet,<br>consectetur adipiscing elit, sed<br>do eiusmod tempor</p>
</div>
<div class="abs service" style="left:520px">
  <div class="ring">
    <svg width="58" height="58" viewBox="0 0 58 58" fill="#555"><circle cx="14" cy="16" r="6"/><circle cx="44" cy="16" r="6"/><path d="M4 40c0-9 4-15 10-15s10 6 10 15zM34 40c0-9 4-15 10-15s10 6 10 15z"/><rect x="14" y="32" width="30" height="4"/><rect x="27" y="36" width="4" height="14"/></svg>
  </div>
  <h3>DISCUSS STRATEGY</h3>
  <p>Lorem ipsum dolor sit amet,<br>consectetur adipiscing elit, sed<br>do eiusmod tempor</p>
</div>

<div class="abs ribbon" style="top:1516px">OUR TEAM</div>

<div class="abs member" style="left:87px;width:316px">
  <div class="photo portrait" role="img" aria-label="Portrait of a male lawyer in a grey suit" style="background:linear-gradient(180deg,#ffffff 0%,#eef0f2 40%,#6b7079 100%)"></div>
  <div class="plate"><h4>TOMAS REUL</h4><span>LAWYER</span></div>
</div>
<div class="abs member active" style="left:441px;width:318px">
  <div class="photo portrait" role="img" aria-label="Portrait of a female lawyer" style="background:linear-gradient(180deg,#f3f3f3 0%,#d9d4cf 50%,#8a8480 100%)"></div>
  <svg class="view-icon" width="40" height="26" viewBox="0 0 40 26"><path d="M20 2C11 2 4 8 1 13c3 5 10 11 19 11s16-6 19-11C36 8 29 2 20 2z" fill="#fff"/><circle cx="20" cy="13" r="6" fill="#5a5a5a"/></svg>
  <div class="plate"><h4>NADIA</h4><span>LAWYER</span></div>
</div>
<div class="abs member" style="left:797px;width:316px">
  <div class="photo portrait" role="img" aria-label="Portrait of a male lawyer in a white shirt and tie" style="background:linear-gradient(180deg,#ffffff 0%,#f1f3f6 45%,#c9d2de 100%)"></div>
  <div class="plate"><h4>TOMAS REUL</h4><span>LAWYER</span></div>
</div>

<div class="abs ribbon" style="top:2089px">LATEST NEWS</div>

<article class="abs news" style="left:85px">
  <div class="photo thumb" role="img" aria-label="Business meeting with documents on a desk" style="background:linear-gradient(135deg,#4a5560 0%,#7b8fa6 50%,#2f5d92 100%)"></div>
  <div class="date">Jan 7, 2017</div>
  <h5>1914 translation by L. Marrow</h5>
  <p>But I must explain to you how all this mistaken idea of denouncing pleasure and praising pain was born and I will give you a complete account of</p>
  <div class="more">Read More</div>
</article>
<article class="abs news active" style="left:437px">
  <div class="photo thumb" role="img" aria-label="Senior businessman at an office desk" style="background:linear-gradient(135deg,#5d6b4e 0%,#c9b8a6 45%,#2d2f33 100%)"></div>
  <div class="date">Jan 6, 2017</div>
  <h5>1914 translation by L. Marrow</h5>
  <p>But I must explain to you how all this mistaken idea of denouncing pleasure and praising pain was born and I will give you a complete account of</p>
  <div class="more">Read More</div>
</article>
<article class="abs news" style="left:787px">
  <div class="photo thumb" role="img" aria-label="Person in a blue suit holding a folder" style="background:linear-gradient(135deg,#1f4f8f 0%,#3a6fb5 50%,#1a3766 100%)"></div>
  <div class="date">Jan 5, 2017</div>
  <h5>1914 translation by L. Marrow</h5>
  <p>But I must explain to you how all this mistaken idea of denouncing pleasure and praising pain was born and I will give you a complete account of</p>
  <div class="more">Read More</div>
</article>

<div class="abs footer"></div>
<div class="abs footer-brand">DRAVIQ</div>
<div class="abs subscribe">
  <div class="field">Subscribe Your Email</div>
  <div class="send"><svg width="20" height="20" viewBox="0 0 20 20"><path d="M1 9 19 1 13 19 10 11z" fill="#fff"/></svg></div>
</div>

<div class="abs reach">
  <h6 class="foot-head">To Reach Us:</h6>
  <ul>
    <li><svg width="10" height="14" viewBox="0 0 10 14"><path d="M5 0a5 5 0 0 0-5 5c0 4 5 9 5 9s5-5 5-9a5 5 0 0 0-5-5z" fill="#333"/><circle cx="5" cy="5" r="2" fill="#d9dadc"/></svg>- 18 Linden Lane, Brookvale, Zurich, 8004.</li>
    <li><svg width="12" height="12" viewBox="0 0 12 12"><path d="M2 0h3l1 3-2 1c1 2 2 3 4 4l1-2 3 1v3c0 1-1 2-2 2C5 12 0 7 0 2 0 1 1 0 2 0z" fill="#333"/></svg>- (041) 555-0192</li>
    <li><svg width="13" height="10" viewBox="0 0 13 10"><rect width="13" height="10" fill="#333"/><path d="M0 0l6.5 5L13 0" stroke="#d9dadc" fill="none"/></svg>- info@draviq.example</li>
  </ul>
</div>

<div class="abs links">
  <h6 class="foot-head">Quick Links:</h6>
  <div class="cols">
    <ul><li>&gt; Home</li><li>&gt; Services</li><li>&gt; Team</li></ul>
    <ul><li>&gt; Careers</li><li>&gt; Blog</li><li>&gt; Contact</li></ul>
  </div>
</div>

<div class="abs bottom"></div>
<div class="abs copy">DRAVIQ © Copyrights 2017. All rights reserved.</div>
<div class="abs social"><span></span><span></span><span></span></div>

</body>
</html>
```